Luxury Caviar Tin Label for High End Caviar Retailer

We are looking for a new caviar label design. We want something unique, preferably black and gold or dark blue and gold. We want a modern and luxurious feel. We have several types of caviar so we need to be able to change the name of the caviar when we print the labels. See inspiration attached. Logo is also attached. More about us: velmoronfare.com

Industry/Entity Type

fine foods industry, caviar

Font styles to use
Serif
Decorative

Requirements
Must have
• KT Velmoron Logo, space for caviar name
Nice to have
• black and gold, blue and gold

```html
<!DOCTYPE html>
<html lang="en">
<head>
<meta charset="utf-8">
<title>KT Velmoron – Osetra Solenne Gold Caviar Label</title>
<link rel="stylesheet" href="https://fonts.googleapis.com/css2?family=Cinzel:wght@400;600&display=swap">
<style>
  :root {
    --backdrop: #0a0a0c;
    --navy: #0d0f1f;
    --navy-deep: #07081a;
    --gold: #d8b24a;
    --gold-light: #fff2a8;
    --gold-mid: #f3d25a;
    --gold-dark: #b88a1c;
    --ink: #1a1406;
  }
  html, body {
    margin: 0;
    width: 1200px;
    height: 1200px;
    overflow: hidden;
    background: var(--backdrop);
  }
  .label {
    display: block;
    width: 1200px;
    height: 1200px;
  }
  .brand-name {
    font-family: "Cinzel", serif;
    font-weight: 400;
    font-size: 52px;
    letter-spacing: 2px;
    fill: var(--gold);
  }
  .caviar-name {
    font-family: "Cinzel", serif;
    font-weight: 600;
    font-size: 74px;
    fill: var(--ink);
  }
  .caviar-type {
    font-family: "Cinzel", serif;
    font-weight: 400;
    font-size: 50px;
    fill: var(--ink);
  }
</style>
</head>
<body>
<svg class="label" viewBox="0 0 1200 1200" xmlns="http://www.w3.org/2000/svg">
  <defs>
    <radialGradient id="band-tone" cx="50%" cy="50%" r="50%">
      <stop offset="75%" stop-color="#2a2616"/>
      <stop offset="90%" stop-color="#3a3218"/>
      <stop offset="100%" stop-color="#1c1a14"/>
    </radialGradient>
    <linearGradient id="gold-field" x1="0" y1="0" x2="0" y2="1">
      <stop offset="0%" stop-color="var(--gold-mid)"/>
      <stop offset="55%" stop-color="var(--gold-light)"/>
      <stop offset="100%" stop-color="var(--gold-mid)"/>
    </linearGradient>
    <clipPath id="inner-disc">
      <circle cx="600" cy="600" r="392"/>
    </clipPath>
  </defs>

  <!-- outer rim -->
  <circle class="rim" cx="600" cy="600" r="530" fill="var(--navy-deep)"/>
  <circle cx="600" cy="600" r="520" fill="none" stroke="var(--gold)" stroke-width="3"/>

  <!-- bubble pattern band -->
  <circle class="bubble-band" cx="600" cy="600" r="515" fill="url(#band-tone)"
          role="img" aria-label="Decorative band of scattered gold caviar-pearl bubbles on dark navy"/>

  <!-- inner frame rings -->
  <circle cx="600" cy="600" r="410" fill="var(--navy)" stroke="var(--gold)" stroke-width="4"/>
  <circle cx="600" cy="600" r="396" fill="none" stroke="var(--gold-dark)" stroke-width="2"/>

  <!-- inner disc: navy top, gold bottom -->
  <g clip-path="url(#inner-disc)">
    <rect x="200" y="200" width="800" height="800" fill="var(--navy)"/>
    <rect class="gold-field" x="200" y="640" width="800" height="400" fill="url(#gold-field)"/>
    <line x1="200" y1="640" x2="1000" y2="640" stroke="var(--gold-dark)" stroke-width="3"/>
  </g>

  <!-- brand -->
  <circle class="brand-mark" cx="600" cy="440" r="70" fill="none" stroke="var(--gold)" stroke-width="3"/>
  <text class="brand-name" x="600" y="600" text-anchor="middle">KT Velmoron</text>

  <!-- caviar name (editable per product) -->
  <text class="caviar-name" x="600" y="740" text-anchor="middle">Osetra Solenne</text>
  <text class="caviar-type" x="600" y="808" text-anchor="middle">Gold Caviar</text>
</svg>
</body>
</html>
```